Brochure Design

I would like to have this brochure design for a approval with the Morvale chamber of commerce . It's a training program for people in Kenya Africa and the gov will pay for the training program. What ever you think would be better let me know. The letters in red are items that are free so I wanted that to stand out. I need to add the logo in the attachment added to the other logos on the front page.

Reason: I'm still looking for the right design and i'm looking to make a quick decision.

```html
<!DOCTYPE html>
<html lang="en">
<head>
<meta charset="utf-8">
<title>Training Program Outline – Aquaculture Spread</title>
<link href="https://fonts.googleapis.com/css2?family=Arimo:wght@400;700&family=Raleway:wght@400&display=swap" rel="stylesheet">
<style>
  :root {
    --backdrop: #e4e1dc;
    --paper: #ffffff;
    --ink: #222222;
    --ink-soft: #555555;
    --label: #6b6b6b;
    --accent: #f4a93c;
    --accent-line: #f7cf95;
    --note-bg: #c9c9c9;
    --photo-light: #b9cbd8;
    --photo-dark: #5d7382;
  }
  * { margin: 0; padding: 0; box-sizing: border-box; }
  html, body { width: 1200px; height: 900px; overflow: hidden; }
  body {
    background: var(--backdrop);
    font-family: "Arimo", Arial, sans-serif;
    color: var(--ink);
    position: relative;
  }
  .page {
    position: absolute;
    top: 52px;
    height: 798px;
    background: var(--paper);
  }
  .page-left { left: 40px; width: 560px; }
  .page-right { left: 600px; width: 568px; }
  .abs { position: absolute; }

  .photo {
    left: 55px; top: 0; width: 223px; height: 118px;
    background: linear-gradient(160deg, var(--photo-light) 0%, #8fa8b8 45%, var(--photo-dark) 100%);
  }
  .body-copy {
    font-size: 11px;
    line-height: 13.4px;
    hyphens: auto;
    -webkit-hyphens: auto;
  }
  .body-copy p + p { margin-top: 6px; }
  .col-a { left: 55px; top: 148px; width: 222px; }
  .col-b { left: 288px; top: 148px; width: 222px; }

  .section-title {
    font-family: "Raleway", "Arimo", sans-serif;
    font-weight: 400;
    font-size: 15.5px;
    line-height: 16px;
    color: var(--ink-soft);
    text-transform: uppercase;
    letter-spacing: 0.3px;
    font-variant-numeric: lining-nums;
    font-feature-settings: "lnum" 1;
  }
  .title-production { left: 55px; top: 460px; }
  .title-cost { left: 58px; top: 70px; }

  .tab {
    width: 155px; height: 15px;
    background: var(--accent);
    font-size: 10.8px; font-weight: 700;
    line-height: 15px;
    padding-left: 6px;
    color: #333;
    border-radius: 0 7px 7px 0;
  }
  .tab-line { font-size: 11px; line-height: 13.4px; hyphens: auto; -webkit-hyphens: auto; }

  .note {
    background: var(--note-bg);
    font-size: 11px;
    line-height: 13.4px;
    padding: 4px 7px;
  }
  .note strong { font-weight: 700; }
  .note-left { left: 55px; top: 646px; width: 456px; }
  .note-right { left: 58px; top: 646px; width: 457px; }

  .cost-item { width: 222px; }
  .cost-label {
    font-size: 10.8px; font-weight: 700;
    color: var(--label);
    padding-bottom: 3px;
    border-bottom: 1.5px solid var(--accent-line);
    margin-bottom: 5px;
  }
  .cost-value { font-size: 11px; line-height: 13.4px; hyphens: auto; -webkit-hyphens: auto; }
  .col-r1 { left: 58px; }
  .col-r2 { left: 292px; }

  .folio {
    font-size: 8.6px;
    color: var(--ink-soft);
    letter-spacing: 0.2px;
  }
  .folio-num { font-size: 11px; }
  .folio-rule { width: 2px; height: 50px; background: var(--accent); }
  .folio strong { font-weight: 700; }
</style>
</head>
<body>

<section class="page page-left">
  <div class="abs photo" role="img" aria-label="Photo of fish packed in ice in harvest crates"></div>

  <div class="abs body-copy col-a">
    <p>The Hydra 2100 system utilizes air to circulate water to the culture tank from the rotary drum filter. The system is designed to provide two “opposing flows” of water, created by compressed air being introduced at the base of each side of the tank. As the air rises through the water it not only provides oxygen but also creates two opposing circulating flows. This circular pattern enables solids to be gently drawn into the outflow ports located at the bottom on both sides of the tank and passed through, intact to the rotary drum filter.</p>
    <p>The unique (patented) dual-current technology also creates a continual current in the culture tank. After the biofilter, the purified water is evenly distributed back into the culture tank, entering from both sides of the tank causing the fish to</p>
  </div>

  <div class="abs body-copy col-b">
    <p>align themselves in the current, constantly swimming “upstream” facing either side of the 40’ long tank. With this constant swimming motion the fish can metabolize the high protein feed into flesh which will give them a higher yield as compared to fish grown in circular aquaculture tanks. Oxygen is injected into the system at three points. One is in the biofilter area where there is 48 feet of dual-current air diffusers. The second is in the culture tank itself where there is 80 feet of dual-current air diffusers. The third is through the airlift water return system. Only one blower is required to handle all three of these processes and can also operate multiple tanks, although a backup is recommended. With this system we have densities of .75 pounds per gallon regularly.</p>
  </div>

  <h2 class="abs section-title title-production">Production Management for<br>Twelve (12) Tank System</h2>

  <div class="abs tab" style="left:55px; top:503px;">Tanks #1 &amp; #2</div>
  <p class="abs tab-line" style="left:55px; top:523px;">18,000 fish in each tank. After 2 months they average .3 pounds.</p>

  <div class="abs tab" style="left:55px; top:546px;">Tanks #3 &amp; #6</div>
  <p class="abs tab-line" style="left:55px; top:567px;">9,000 fish in each tank. After 2 months they average .75 pounds.</p>

  <div class="abs tab" style="left:55px; top:590px;">Tanks #7 &amp; #12</div>
  <p class="abs tab-line" style="left:55px; top:610px; width:456px;">6,000 fish in each tank. After 2 months they average 1.25 pounds. Harvest 12 aquaculture tanks at 7,500 pounds per tank 3 times a year or 270,000 pounds per year.</p>

  <p class="abs note note-left"><strong>Note:</strong> This management technique is one that has been used for decades called “Stock Splitting”. Fingerlings are contracted from a hatchery for a ten week delivery schedule or ponds are installed for the facilities own production.</p>

  <div class="abs folio-rule" style="left:34px; top:748px;"></div>
  <p class="abs folio" style="left:17px; top:766px;"><span class="folio-num">12</span></p>
  <p class="abs folio" style="left:43px; top:767px;"><strong>NORTHBRIDGE MOBILITY GROUP</strong> TRAINING PROGRAM OUTLINE</p>
</section>

<section class="page page-right">
  <h2 class="abs section-title title-cost">Operation Cost for Twelve<br>(12) Tank System</h2>

  <div class="abs cost-item col-r1" style="top:113px;">
    <p class="cost-label">Electric</p>
    <p class="cost-value">$1,800 per month with an electric rate of $0.10 per KWH or $21,600 per year</p>
  </div>
  <div class="abs cost-item col-r1" style="top:170px;">
    <p class="cost-label">Fingerlings</p>
    <p class="cost-value">216,000 fish at $0.10 each = $21,600 per year</p>
  </div>
  <div class="abs cost-item col-r1" style="top:224px;">
    <p class="cost-label">Food</p>
    <p class="cost-value">270,000 pounds of fish x 1.3 FCR (Food Conversion Rate) x $0.32 per pound of food = $112,320 per year (It requires 1.3 lbs of food to make 1 lb of fish)</p>
  </div>
  <div class="abs cost-item col-r1" style="top:301px;">
    <p class="cost-label">Heat</p>
    <p class="cost-value">10,000 SQFT building heated with waste motor oil at $0.50 per gallon using 3,000 gallons per year = $1,500 per year</p>
  </div>
  <div class="abs cost-item col-r1" style="top:367px;">
    <p class="cost-label">Property Tax:</p>
    <p class="cost-value">$2,500 per year</p>
  </div>
  <div class="abs cost-item col-r1" style="top:409px;">
    <p class="cost-label">Sewer Tax</p>
    <p class="cost-value">$5,800 per year</p>
  </div>
  <div class="abs cost-item col-r1" style="top:454px;">
    <p class="cost-label">Insurance</p>
    <p class="cost-value">Building and Fish Mortality = $8,000 per year</p>
  </div>
  <p class="abs cost-value col-r1" style="top:536px;">Breakeven will occur in 21.5 months.</p>

  <div class="abs cost-item col-r2" style="top:113px;">
    <p class="cost-label">Miscellaneous</p>
    <p class="cost-value">Soda Ash, Salt, Testing Chemicals = $15,000 per year</p>
  </div>
  <div class="abs cost-item col-r2" style="top:170px;">
    <p class="cost-label">Labor</p>
    <p class="cost-value">Part time 20 hours per week (grading and harvest) $10.00 per hour or $10,400 per year</p>
  </div>
  <div class="abs cost-item col-r2" style="top:237px;">
    <p class="cost-label">Maintenance</p>
    <p class="cost-value">Little to no maintenance is required because there are no moving parts. Rotary drum filter or blower may need to be replaced, but that is a rare occurrence.</p>
  </div>
  <div class="abs cost-item col-r2" style="top:321px;">
    <p class="cost-label">One Time Cost</p>
    <p class="cost-value">$730,000* for 12 tank system</p>
  </div>
  <div class="abs cost-item col-r2" style="top:366px;">
    <p class="cost-label">Total Annual Cost</p>
    <p class="cost-value">$200,270 (cost per pound $0.74)</p>
  </div>
  <div class="abs cost-item col-r2" style="top:410px;">
    <p class="cost-label">Average Selling Price</p>
    <p class="cost-value">$2.25 per pound x 270,000 pounds per year = $607,500 per year</p>
  </div>
  <div class="abs cost-item col-r2" style="top:466px;">
    <p class="cost-label">Net Profit</p>
    <p class="cost-value">$607,500 Revenue – $200,270 Costs = $407,230</p>
  </div>
  <p class="abs cost-value col-r2" style="top:536px; width:224px;">*One-time costs reflect the cost of the equipment only, and not the cost to deliver or set up the equipment. Additional details available upon request.</p>

  <p class="abs note note-right"><strong>Note:</strong> These cost and production data are shown as an example of operating an aquaculture tank facility. Actual results may vary from state to state due to food cost, electric rate, insurance, labor and sale price which will affect the business profitability.</p>

  <div class="abs folio-rule" style="left:533px; top:748px;"></div>
  <p class="abs folio" style="left:542px; top:766px;"><span class="folio-num">13</span></p>
</section>

</body>
</html>
```